Tarvo Mosquito Repellent Oil made from 100% Essential Oils

I want someone to design a label for a product for me. Here are the details of the project.

Mosquito Project A: The project name is called Tarvo. It's a mixture of 100% Essential Oils (about 14 of them to be exact) into one bottle. The bottle sizes will start from 3 milliliters, 5 milliliters, 10 milliliters and 20 milliliters and 30 milliliters (1 fl. oz.)

I want the label to have the Tarvo logo. You will have to create this logo from scratch. I don't have a logo now.

Here are the requirements:
1.0 Logo for Tarvo
1.1 100% pure essential oils
1.2 Net (size of the bottle)

1.3 Ingredients:
1.3a Citronella Oil
1.3b Neem Oil
1.3c Lemon grass Oil
1.3d Eucalyptus Oil

2.0 Aroma: Spicy

3.0 Benefits: Repel mosquitoes

4.0 Mixes Well With:
4.1 Shea Butter
4.2 Olive Oil

5.0 Extraction Method: Steam Distilled from plant's leaves and twigs.

6.0 Barcode Label

7.0 Address: Tarvo Mosquito Oils, LLC. 4807 Orchard Mill Rd. McLean, VA 22847
7.1 Website: www.tarvobugcare.example

8.0 Suggested Use: For external use only. Rub in your hands and gently apply it to your hands, legs and around your neck and ears. Apply it to scent. When mixing with Shea Butter, use about 4 drops with 20 milliliters of Shea Butter. When mixing with Olive Oil, use about 4 drops with 20 milliliters of Olive Oil.

9.0 Natural essential oils are highly concentrated and should be used with care.

10.0 Caution: Keep out of reach of children. Avoid contact with eyes. If pregnant or lactating, consult your healthcare practitioner before using. Do not eat.

Attached is how the bottles will look like.

Thank you,

Dorn

Target Market(s)

Countries with high rate of malaria, a mosquito-borne diseases.

Industry/Entity Type

Product

Logo Text

Tarvo

Font styles to use
Sans Serif
Script

Colors
ec1f27
faa54b
33a6d7

Requirements
Must have
• A logo, a website, a label for all the different bottle sizes. I have attached a logo of the "Veyla" bug repellent, I like that, it's nice and simple.
Nice to have
• I don't know, think of something that will be nice to have.
Should not have
• I don't know.

```html
<!DOCTYPE html>
<html lang="en">
<head>
<meta charset="utf-8">
<title>Tarvo Mosquito Repellent Oil – Box Label</title>
<link rel="stylesheet" href="https://fonts.googleapis.com/css2?family=Oswald:wght@400;500;700&display=swap">
<style>
  :root {
    --red: #ef5656;
    --red-deep: #ec1f27;
    --blue: #5fb3e0;
    --blue-deep: #33a6d7;
    --yellow: #fcd434;
    --orange: #faa54b;
    --ink: #111111;
    --paper: #ffffff;
  }
  html, body {
    margin: 0;
    padding: 0;
    width: 1200px;
    height: 1200px;
    overflow: hidden;
    background: var(--paper);
  }
  .canvas {
    position: relative;
    width: 1200px;
    height: 1200px;
    font-family: "Oswald", "Arial Narrow", sans-serif;
  }
  .box-label {
    position: absolute;
    left: 130px;
    top: 100px;
    display: flex;
    height: 1000px;
    box-shadow: 0 14px 30px rgba(0,0,0,0.12);
  }

  /* Front panel */
  .front-panel {
    position: relative;
    width: 580px;
    height: 1000px;
    overflow: hidden;
  }
  .front-art {
    position: absolute;
    inset: 0;
    width: 580px;
    height: 1000px;
    display: block;
  }
  .brand-logo {
    position: absolute;
    left: 0;
    right: 0;
    top: 380px;
    margin: 0;
    display: flex;
    justify-content: center;
    align-items: center;
    gap: 22px;
  }
  .brand-mark {
    width: 40px;
    height: 40px;
    border-radius: 50%;
    background: var(--yellow);
  }
  .brand-name {
    margin: 0;
    font-size: 120px;
    font-weight: 700;
    line-height: 1;
    letter-spacing: 2px;
    color: var(--ink);
    text-transform: uppercase;
  }
  .net-size {
    position: absolute;
    left: 0;
    right: 0;
    top: 530px;
    margin: 0;
    text-align: center;
    font-size: 26px;
    font-weight: 500;
    letter-spacing: 2px;
    color: var(--paper);
    text-transform: uppercase;
  }
  .product-type {
    position: absolute;
    left: 0;
    right: 0;
    bottom: 82px;
    margin: 0;
    text-align: center;
    font-size: 50px;
    font-weight: 700;
    line-height: 1;
    color: var(--ink);
    text-transform: uppercase;
  }
  .product-claim {
    position: absolute;
    left: 0;
    right: 0;
    bottom: 34px;
    margin: 0;
    text-align: center;
    font-size: 32px;
    font-weight: 400;
    letter-spacing: 2px;
    line-height: 1;
    color: var(--ink);
    text-transform: uppercase;
  }

  /* Side panel */
  .side-panel {
    position: relative;
    width: 360px;
    height: 1000px;
    overflow: hidden;
  }
  .side-bg {
    position: absolute;
    inset: 0;
    width: 360px;
    height: 1000px;
    display: block;
  }
  .side-content {
    position: relative;
    box-sizing: border-box;
    height: 1000px;
    padding: 30px 28px 24px;
    display: flex;
    flex-direction: column;
    gap: 14px;
  }
  .info-block { margin: 0; color: var(--ink); }
  .info-block.ingredients { color: var(--paper); margin-bottom: 34px; }
  .info-title {
    margin: 0 0 2px;
    font-size: 19px;
    font-weight: 700;
    line-height: 1.3;
  }
  .info-list {
    list-style: none;
    margin: 0;
    padding: 0;
    font-size: 17px;
    font-weight: 400;
    line-height: 1.4;
  }
  .fine-print {
    margin: 0;
    font-size: 13px;
    font-weight: 400;
    line-height: 1.38;
  }
  .fine-print strong { font-weight: 700; }
  .company {
    margin-top: auto;
    font-size: 13px;
    line-height: 1.4;
    font-style: normal;
  }
  .company .web { font-weight: 500; }
</style>
</head>
<body>
<main class="canvas">
  <section class="box-label">
    <article class="front-panel">
      <svg class="front-art" viewBox="0 0 580 1000" role="img" aria-label="Comic pop-art burst illustration: red and blue radiating rays with a yellow lightning bolt, stars and a mosquito over a yellow explosion">
        <rect width="580" height="1000" fill="var(--blue)"/>
        <polygon points="0,0 580,0 580,420 0,640" fill="var(--red)"/>
        <polygon points="0,790 580,760 580,1000 0,1000" fill="var(--yellow)"/>
      </svg>
      <div class="brand-logo">
        <span class="brand-mark"></span>
        <h1 class="brand-name">Tarvo</h1>
      </div>
      <p class="net-size">Net 30 mL (1 fl. oz.)</p>
      <p class="product-type">Mosquito Repellent Oil</p>
      <p class="product-claim">100% Pure Essential Oils</p>
    </article>

    <aside class="side-panel">
      <svg class="side-bg" viewBox="0 0 360 1000" aria-hidden="true">
        <rect width="360" height="1000" fill="var(--blue-deep)"/>
        <polygon points="0,0 360,0 360,200 0,250" fill="var(--red)"/>
      </svg>
      <div class="side-content">
        <div class="info-block ingredients">
          <h2 class="info-title">Ingredients:</h2>
          <ul class="info-list">
            <li>Citronella Oil</li>
            <li>Neem Oil</li>
            <li>Lemon grass Oil</li>
            <li>Eucalyptus Oil</li>
          </ul>
        </div>
        <div class="info-block">
          <h2 class="info-title">Aroma:</h2>
          <ul class="info-list"><li>Spicy</li></ul>
        </div>
        <div class="info-block">
          <h2 class="info-title">Benefits:</h2>
          <ul class="info-list"><li>Repel mosquitoes</li></ul>
        </div>
        <div class="info-block">
          <h2 class="info-title">Mixes Well With:</h2>
          <ul class="info-list">
            <li>Shea Butter</li>
            <li>Olive Oil</li>
          </ul>
        </div>
        <div class="info-block">
          <h2 class="info-title">Extraction Method:</h2>
          <p class="fine-print">Steam distilled from plant's leaves and twigs.</p>
        </div>
        <div class="info-block">
          <h2 class="info-title">Suggested Use:</h2>
          <p class="fine-print">For external use only. Rub in your hands and gently apply it to your hands, legs and around your neck and ears. Apply it to scent. When mixing with Shea Butter, use about 4 drops with 20 mL of Shea Butter. When mixing with Olive Oil, use about 4 drops with 20 mL of Olive Oil.</p>
        </div>
        <div class="info-block">
          <p class="fine-print">Natural essential oils are highly concentrated and should be used with care.</p>
          <p class="fine-print"><strong>Caution:</strong> Keep out of reach of children. Avoid contact with eyes. If pregnant or lactating, consult your healthcare practitioner before using. Do not eat.</p>
        </div>
        <address class="info-block company">
          Tarvo Mosquito Oils, LLC.<br>
          4807 Orchard Mill Rd. McLean, VA 22847<br>
          <span class="web">www.tarvobugcare.example</span>
        </address>
      </div>
    </aside>
  </section>
</main>
</body>
</html>
```